Refresh of graphic design for existing website

We would like to refresh our website. Please see the attached design specifications.

Industry/Entity Type

Graphic Design

```html
<!DOCTYPE html>
<html lang="en">
<head>
<meta charset="utf-8">
<title>The Service Gear Institute</title>
<link rel="stylesheet" href="https://fonts.googleapis.com/css2?family=Open+Sans:wght@400;600;700&display=swap">
<style>
:root{
  --navy:#1c3d6e;
  --navy-dark:#16325c;
  --blue:#2b8fd0;
  --blue-text:#2a78b8;
  --green:#7cc21f;
  --green-dark:#5f9c12;
  --gray-band:#e9eaec;
  --card:#ffffff;
  --line:#d3d7dc;
  --text:#555b63;
  --heading:#1f4f86;
  --white:#fff;
}
*{box-sizing:border-box;margin:0;padding:0}
html,body{width:1200px;height:2320px;overflow:hidden}
body{font-family:"Open Sans",Arial,sans-serif;color:var(--text);background:#fff;position:relative}
a{color:inherit;text-decoration:none}

.topbar{height:28px;background:var(--navy);color:#fff;font-size:12px;display:flex;align-items:center;justify-content:space-between;padding:0 28px}
.topbar .account span{margin-right:14px}
.social{display:flex;gap:8px}
.social i{width:14px;height:14px;border-radius:50%;background:#fff;opacity:.85;display:block}

.nav{height:92px;display:flex;align-items:center;justify-content:space-between;padding:0 28px;border-bottom:1px solid #eee}
.brand{display:flex;align-items:center;gap:10px;font-weight:700;font-size:30px;color:var(--blue)}
.brand i{width:18px;height:18px;border-radius:50%;background:var(--green);display:block}
.menu{display:flex;gap:34px;font-size:14px;color:var(--blue-text)}

.hero{position:relative;height:380px;background:linear-gradient(120deg,#1a1d22 0%,#4a4f57 35%,#7d8289 55%,#3a3e45 80%,#15171b 100%)}
.hero .arrow{position:absolute;top:170px;width:26px;height:40px}
.hero .arrow.left{left:10px}.hero .arrow.right{right:10px}
.dots{position:absolute;bottom:14px;left:50%;transform:translateX(-50%);display:flex;gap:8px}
.dots i{width:10px;height:10px;border-radius:50%;background:#fff;opacity:.6;display:block}
.dots i:first-child{opacity:1}

.banner{height:120px;background:var(--green);text-align:center;padding-top:26px}
.banner h1{font-size:34px;color:#17324f;font-weight:700}
.banner p{font-size:18px;color:#fff;margin-top:8px}

.welcome{display:flex;gap:28px;padding:34px 88px 0}
.welcome .photo{width:252px;height:228px;background:linear-gradient(135deg,#9aa3ad,#4d5560 60%,#2c3138)}
.welcome .body{flex:1;padding-top:10px}
.welcome small{font-size:14px;color:var(--blue-text);text-transform:uppercase}
.welcome h2{font-size:24px;color:var(--blue-text);font-weight:700;margin:4px 0 14px}
.welcome p{font-size:12px;line-height:1.6}
.btn{display:inline-block;background:var(--green);color:#fff;font-size:12px;padding:6px 14px;border-radius:2px}
.welcome .btn{margin-top:16px}

.events{position:absolute;top:928px;left:0;width:1200px;height:560px;background:var(--gray-band)}
.section-title{text-align:center;font-size:30px;font-weight:700;color:var(--heading)}
.events .section-title{margin-top:40px}
.cards{display:grid;grid-template-columns:504px 504px;gap:24px 24px;justify-content:center;margin-top:26px}
.card{background:var(--card);height:208px;text-align:center;display:flex;flex-direction:column}
.card h3{font-size:15px;color:var(--blue-text);font-weight:600;margin:24px 0 10px;text-transform:uppercase}
.card p{font-size:12px;line-height:1.7;padding:0 40px;flex:1}
.card .btn{display:block;border-radius:0;padding:9px 0}

.news{position:absolute;top:1530px;left:88px;width:1024px}
.news .section-title{margin-bottom:28px}
.row{height:40px;border:1px solid var(--line);display:flex;align-items:center;justify-content:space-between;padding:0 16px;font-size:12px;color:var(--blue-text);margin-bottom:32px}
.row .date{color:#8a9097;margin-left:8px}
.row.open{margin-bottom:8px}
.row svg{width:14px;height:14px}
.news .expanded{font-size:12px;line-height:1.7;margin-bottom:26px}

.quick{position:absolute;top:2140px;left:0;width:1200px;text-align:center}
.quick ul{list-style:none;display:flex;flex-wrap:wrap;justify-content:center;gap:10px 28px;width:820px;margin:22px auto 0;font-size:12px}
.quick li::before{content:"";display:inline-block;width:6px;height:6px;border-radius:50%;background:var(--green);margin-right:7px;vertical-align:middle}

.footer{position:absolute;top:2252px;left:0;width:1200px;height:68px;background:var(--navy);color:#fff;font-size:11px;padding:14px 28px 0}
.footer .links{display:flex;justify-content:space-between}
.footer .links nav{display:flex;gap:30px}
.footer .bottom{display:flex;justify-content:space-between;margin-top:14px;opacity:.85}
</style>
</head>
<body>
<header>
  <div class="topbar">
    <div class="account"><span>Join SGI</span><span>Login ▾</span></div>
    <div class="social"><i></i><i></i><i></i><i></i></div>
  </div>
  <div class="nav">
    <div class="brand"><i></i>sgi</div>
    <nav class="menu"><a>Home</a><a>About</a><a>Membership</a><a>SGI Members</a><a>SGI Events</a><a>Tech Library</a><a>Market Research</a><a>Contact</a></nav>
  </div>
</header>

<section class="hero" role="img" aria-label="Mechanic working on a car engine with a wrench">
  <svg class="arrow left" viewBox="0 0 26 40"><path d="M18 8 L8 20 L18 32" fill="none" stroke="#fff" stroke-width="3"/></svg>
  <svg class="arrow right" viewBox="0 0 26 40"><path d="M8 8 L18 20 L8 32" fill="none" stroke="#fff" stroke-width="3"/></svg>
  <div class="dots"><i></i><i></i><i></i></div>
</section>

<section class="banner">
  <h1>The Service Gear Institute</h1>
  <p>Serving the Automotive Repair Industry Since 1947</p>
</section>

<section class="welcome">
  <div class="photo" role="img" aria-label="Technician using a diagnostic tool in a workshop"></div>
  <div class="body">
    <small>Welcome to our website</small>
    <h2>The Service Gear Institute</h2>
    <p>Our members build the tools, equipment and software that keep repair shops running. We bring makers and technicians together to share data, set common standards and help every workshop fix modern vehicles right the first time. Learn how we work with industry partners and how your company can take part in our programs.</p>
    <a class="btn">Read More ▸</a>
  </div>
</section>

<section class="events">
  <h2 class="section-title">Upcomming events</h2>
  <div class="cards">
    <div class="card"><h3>Lorem ipsum is simply</h3><p>Join members for a day of talks on shop tools, new vehicle systems and data access. Sessions cover training, standards work and the year ahead for the repair trade.</p><a class="btn">Read More ▸</a></div>
    <div class="card"><h3>Lorem ipsum is simply</h3><p>Join members for a day of talks on shop tools, new vehicle systems and data access. Sessions cover training, standards work and the year ahead for the repair trade.</p><a class="btn">Read More ▸</a></div>
    <div class="card"><h3>Lorem ipsum is simply</h3><p>Join members for a day of talks on shop tools, new vehicle systems and data access. Sessions cover training, standards work and the year ahead for the repair trade.</p><a class="btn">Read More ▸</a></div>
    <div class="card"><h3>Lorem ipsum is simply</h3><p>Join members for a day of talks on shop tools, new vehicle systems and data access. Sessions cover training, standards work and the year ahead for the repair trade.</p><a class="btn">Read More ▸</a></div>
  </div>
</section>

<section class="news">
  <h2 class="section-title">Industry News</h2>
  <div class="row open"><span>Contrary to popular belief, Lorem Ipsum is not simply random text.<span class="date">25th September 2015</span></span><svg viewBox="0 0 14 14"><circle cx="7" cy="7" r="6" fill="#8a9097"/><path d="M4 7h6" stroke="#fff" stroke-width="2"/></svg></div>
  <p class="expanded">Shop owners report steady growth in demand for diagnostic service as new vehicles reach the road with more electronic systems. Members met this month to review shared test methods, update training material and plan a joint survey of repair shops. Results will guide the next round of standards work and help tool makers plan products for the coming model years. Full details are in the member area.</p>
  <div class="row"><span>Contrary to popular belief, Lorem Ipsum is not simply random text.<span class="date">25th September 2015</span></span><svg viewBox="0 0 14 14"><circle cx="7" cy="7" r="6" fill="#8a9097"/><path d="M4 7h6M7 4v6" stroke="#fff" stroke-width="2"/></svg></div>
  <div class="row"><span>Contrary to popular belief, Lorem Ipsum is not simply random text.<span class="date">25th September 2015</span></span><svg viewBox="0 0 14 14"><circle cx="7" cy="7" r="6" fill="#8a9097"/><path d="M4 7h6M7 4v6" stroke="#fff" stroke-width="2"/></svg></div>
  <div class="row"><span>Contrary to popular belief, Lorem Ipsum is not simply random text.<span class="date">25th September 2015</span></span><svg viewBox="0 0 14 14"><circle cx="7" cy="7" r="6" fill="#8a9097"/><path d="M4 7h6M7 4v6" stroke="#fff" stroke-width="2"/></svg></div>
  <div class="row"><span>Contrary to popular belief, Lorem Ipsum is not simply random text.<span class="date">25th September 2015</span></span><svg viewBox="0 0 14 14"><circle cx="7" cy="7" r="6" fill="#8a9097"/><path d="M4 7h6M7 4v6" stroke="#fff" stroke-width="2"/></svg></div>
  <div class="row"><span>Contrary to popular belief, Lorem Ipsum is not simply random text.<span class="date">25th September 2015</span></span><svg viewBox="0 0 14 14"><circle cx="7" cy="7" r="6" fill="#8a9097"/><path d="M4 7h6M7 4v6" stroke="#fff" stroke-width="2"/></svg></div>
</section>

<section class="quick">
  <h2 class="section-title">Quick Links</h2>
  <ul>
    <li>Contrary to popular belief</li><li>The standard chunk</li><li>Lorem Ipsum used</li><li>The standard chunk</li><li>Contrary to popular belief</li>
    <li>The standard chunk</li><li>There are many variations</li><li>The standard chunk</li><li>Contrary to popular belief</li>
  </ul>
</section>

<footer class="footer">
  <div class="links">
    <nav><a>Home</a><a>About</a><a>Membership</a><a>SGI Members</a><a>SGI Events</a><a>Tech Library</a><a>Market Research</a><a>Contact</a></nav>
    <nav><a>Privacy policy</a><a>Terms of Use</a></nav>
  </div>
  <div class="bottom"><span>Copyright © 2015 The Service Gear Institute. All Rights Reserved.</span><span></span></div>
</footer>
</body>
</html>
```